Webdesign für lokalen Haushersteller
Zielgruppe
Wir sind ein lokaler Haushersteller
Siehe auch https://www.lemar-steinheim.de/unternehmen/kamp-lintfort/kv-werkbau-gmbh/partner/
Aufgabenstellung
Hallo, wir benötigen eine landingpage wie z.b. Hier.
Wir müssen immer wieder einzelne Baugebiete bewerben. Dazu hätten wir gerne eine ähnliche Seite mit kontaktformular usw. bitte als Farbe und Logo die Referenz von unserer Hauptseite nehmen. Das design sollt modern sein.
Am besten wäre denke ich eine Lösung mit WordPress,dann könnten wir aktuelle Baugrundstücke auf diese Seite selber pflegen
https://www.tq-wohnbau.de/baugebiet-wesel.html

```html
<!DOCTYPE html>
<html lang="de">
<head>
<meta charset="utf-8">
<title>KV Werkbau – Lemar Bausatzhaus Partner</title>
<link href="https://fonts.googleapis.com/css2?family=Poppins:wght@300;400;500;600&display=swap" rel="stylesheet">
<style>
:root{
  --yellow:#f9b91c;
  --cream:#fde8c2;
  --stage:#e6e6e6;
  --white:#ffffff;
  --ink:#1e1e1e;
  --panel:#ebeae8;
  --field:#f5f5f3;
  --footer:#8f8f8f;
  --footer-text:#f0f0f0;
}
*{margin:0;padding:0;box-sizing:border-box}
html,body{width:1200px;height:2413px;overflow:hidden;background:var(--stage)}
body{font-family:'Poppins',sans-serif;color:var(--ink);position:relative}
.page{position:absolute;left:94px;top:123px;width:1028px;height:2203px;background:var(--white)}
.nav a{position:absolute;top:38px;font-size:13px;text-decoration:none;color:var(--ink);letter-spacing:.2px}
.logo-tab{position:absolute;left:457px;top:19px;width:111px;height:102px;background:#bdbdbd}
.logo{position:absolute;left:468px;top:29px;width:91px;height:92px;background:var(--yellow);display:flex;flex-direction:column;align-items:center;justify-content:center;z-index:2}
.logo span{font-size:16px;font-weight:600;color:var(--white);letter-spacing:.5px;line-height:1.1}
.hero{position:absolute;left:0;top:76px;width:1028px;height:502px;overflow:hidden}
.hero-photo{position:absolute;inset:0;background:linear-gradient(180deg,#d9dbd9 0%,#cfcfca 45%,#b5b3a9 68%,#8f9a6e 86%,#7b8a5a 100%)}
.hero-veil{position:absolute;inset:0;background:rgba(255,255,255,.25)}
.hero h1{position:absolute;top:187px;width:100%;text-align:center;font-size:42px;font-weight:600;color:var(--white);letter-spacing:.5px}
.hero p{position:absolute;top:240px;width:100%;text-align:center;font-size:21px;color:var(--white)}
.btn{position:absolute;background:var(--yellow);color:var(--white);font-size:14px;font-weight:500;display:flex;align-items:center;justify-content:center;letter-spacing:.5px;border-radius:2px}
.badge{position:absolute;left:827px;top:483px;width:134px;height:134px;border-radius:50%;background:#8a8a8a;border:4px solid var(--white);z-index:3;overflow:hidden}
.badge div{position:absolute;left:2px;top:40px;width:130px;transform:rotate(22deg);text-align:center;line-height:1.2}
.badge .a{font-size:14px;color:var(--white)}
.badge .b{font-size:17px;font-weight:600;color:var(--yellow)}
h2{position:absolute;width:100%;text-align:center;font-size:21px;font-weight:500;letter-spacing:.3px}
.copy{position:absolute;width:100%;text-align:center;font-size:12px;line-height:15px}
.copy p{margin-bottom:14px}
.svc{position:absolute;top:886px;height:328px;background:var(--cream)}
.svc-title{position:absolute;top:886px;left:14px;width:239px;height:97px;background:var(--cream);display:flex;align-items:center;justify-content:center;text-align:center;font-size:21px;font-weight:500;line-height:26px}
.svc-photo{position:absolute;left:14px;top:1000px;width:239px;height:214px;background:linear-gradient(180deg,#c9cfd2 0%,#e3e6e7 55%,#b9b7b2 100%)}
.svc svg{position:absolute;left:50%;top:18px;transform:translateX(-50%)}
.svc h3{position:absolute;top:62px;width:100%;text-align:center;font-size:12px;font-weight:600;line-height:15px}
.svc ul{position:absolute;top:118px;left:20px;right:14px;list-style:none;font-size:11px;line-height:13px}
.svc li{margin-bottom:8.5px;padding-left:7px;text-indent:-7px}
.svc li::before{content:"• "}
.proj{position:absolute;background:linear-gradient(180deg,#7fb0dc 0%,#cfe0ec 40%,#e9e9e6 62%,#6f8d4b 100%)}
.plus{position:absolute;width:28px;height:28px}
.proj-head{position:absolute;left:326px;top:1531px;width:383px;height:37px;background:var(--panel);display:flex;align-items:center;justify-content:center;font-size:21px;font-weight:500}
.plan{position:absolute;left:562px;top:1584px;width:147px;height:146px;background:#fbf1d9;border:2px solid var(--yellow)}
.contact-card{position:absolute;left:14px;top:1800px;width:239px;height:260px;background:var(--panel)}
.contact-card h4{position:absolute;top:30px;width:100%;text-align:center;font-size:21px;font-weight:500}
.contact-card .info{position:absolute;left:17px;top:78px;font-size:12px;line-height:21.5px}
.form{position:absolute;left:270px;top:1800px;width:735px;height:260px;background:var(--panel)}
.field{position:absolute;background:var(--field);font-size:12px;padding:11px 11px;color:var(--ink)}
.footer{position:absolute;left:0;top:2075px;width:1028px;height:128px;background:var(--footer)}
.footer-logo{position:absolute;left:16px;top:18px;width:91px;height:91px;background:var(--yellow);display:flex;flex-direction:column;align-items:center;justify-content:center}
.footer-logo span{font-size:15px;font-weight:600;color:var(--white);line-height:1.1}
.footer h5{position:absolute;top:26px;font-size:17px;font-weight:500;color:var(--yellow);letter-spacing:.3px}
.footer .links{position:absolute;font-size:12px;line-height:21.5px;color:var(--footer-text)}
.social{position:absolute;top:51px;width:47px;height:47px;background:var(--yellow)}
</style>
</head>
<body>
<div class="page">
  <nav class="nav">
    <a style="left:149px">ÜBER UNS</a>
    <a style="left:237px">LEISTUNGEN</a>
    <a style="left:343px">BAUPROJEKTE</a>
    <a style="left:593px">TERMINE</a>
    <a style="left:681px">UNSERE HÄUSER</a>
    <a style="left:817px">KONTAKT</a>
  </nav>
  <div class="logo-tab"></div>
  <div class="logo"><span>LEMAR</span><span style="font-size:10px;font-weight:600">Bausatzhaus</span></div>

  <section class="hero">
    <div class="hero-photo" role="img" aria-label="Modernes eingeschossiges Flachdachhaus mit Terrasse, Pool, Sesseln und Rasen"></div>
    <div class="hero-veil"></div>
    <h1>WILLKOMMEN IN KV WERKBAU</h1>
    <p>Ihr Partner vor Ort - Kompetenz in Ihrer Nähe</p>
    <div class="btn" style="left:414px;top:363px;width:199px;height:39px">UNSER PORTFOLIO</div>
  </section>
  <div class="badge"><div><span class="a">Bezugsfertig in</span><br><span class="b">5 MONATEN</span></div></div>

  <h2 style="top:620px">ÜBER UNS</h2>
  <div class="copy" style="top:671px">
    <p>Ihre Wünsche, Fähigkeiten, Ressourcen und unsere Kompetenzen sind die sichere Basis für die Erfüllung Ihres Traumes. Gemeinsam gestalten wir Ihr<br>hochwertiges, massives, energieeffizientes Eigenheim individuell nach Ihren Vorstellungen – und zwar zu einem exzellenten Preis-Leistungs-Verhältnis!</p>
    <p>1980 wurde unser Unternehmen gegründet. Mittlerweile sind wir in unserer Region marktführend.<br>Wir sind Ihr Lemar Bausatzhauspartner in folgenden Regionen: Kreis Wesel, Kreis Kleve, Krefeld, Mönchengladbach und die Niederlande.</p>
    <p>Verlassen Sie sich auf einen starken Partner – verlassen Sie sich auf uns!</p>
  </div>
  <div class="btn" style="left:414px;top:805px;width:199px;height:38px">UNSER TEAM</div>

  <div class="svc-title">UNSERE<br>LEISTUNGEN</div>
  <div class="svc-photo" role="img" aria-label="Wohnraum mit Lounge-Sessel, Palme und Bergpanorama hinter großer Glasfront"></div>

  <div class="svc" style="left:268px;width:239px">
    <svg width="30" height="34" viewBox="0 0 30 34" fill="none" stroke="#1e1e1e" stroke-width="1.6"><path d="M3 15 L15 4 L27 15 V31 H3 Z"/><path d="M12 31 V22 H18 V31"/></svg>
    <h3>AUSWAHL- UND<br>BERATUNGSPHASE</h3>
    <ul>
      <li>Bedarfsanalyse</li><li>Grundstückserwerb</li><li>Entwurfsplanung</li><li>Angebotserstellung und -prüfung</li><li>Finanzierungsplanung</li><li>Vertragsabschluss und -bestätigung</li><li>Rücktrittsrecht innerhalb von 14 Tagen</li>
    </ul>
  </div>
  <div class="svc" style="left:521px;width:239px">
    <svg width="36" height="36" viewBox="0 0 36 36" fill="none" stroke="#1e1e1e" stroke-width="1.6"><path d="M3 14 L25 30 L33 22 L11 6 Z"/><path d="M9 12 L12 10 M13 15 L16 13 M17 18 L20 16 M21 21 L24 19"/><path d="M18 14 L30 2 L34 6 L22 18"/></svg>
    <h3>PLANUNGS- UND<br>BAUVORBEREITUNGSPHASE</h3>
    <ul>
      <li>Statische Berechnungen</li><li>Bauantragsplanung</li><li>Baugenehmigungsverfahren</li><li>Festlegung der Ausstattungsdetails</li><li>Baugenehmigung</li><li>Abgabe Festpreisgarantie</li><li>Ausstellung des Eigenleistungsnachweises</li><li>Finanzierungsvermittlung</li><li>Ablaufplan mit Bauterminen</li>
    </ul>
  </div>
  <div class="svc" style="left:775px;width:239px">
    <svg width="30" height="30" viewBox="0 0 30 30" fill="none" stroke="#1e1e1e" stroke-width="1.6"><rect x="3" y="4" width="24" height="22" rx="2"/><path d="M3 11 H27 M3 18 H27 M11 4 V11 M19 11 V18 M11 18 V26"/></svg>
    <h3 style="top:70px">HAUSBAUPHASE</h3>
    <ul>
      <li>Materialanlieferungen nach Abruf</li><li>Betreuung durch den Lemar</li><li>Bausatzhaus Partner</li><li>Bausätze und schlüsselfertiges</li><li>Bauen</li><li>Glasdichter Rohbau</li><li>Richtfest</li><li>Komplette Erstellung</li>
    </ul>
  </div>

  <h2 style="top:1262px">FINANZIERUNG &amp; VERSICHERUNG</h2>
  <div class="copy" style="top:1316px;left:20px;width:988px">
    <p>Gerne unterstützen wir Sie bei der Beantragung von Fördermitteln, wie z.B. bei der Förderbank für Wohnbau (FWB) oder vermitteln Sie auch direkt zu einen<br>unserer Spezialist für Baufinanzierungen.</p>
    <p>Bitte sprechen Sie uns im Rahmen der genannten Versicherungsleistungen an, unsere Experten aus dem Versicherungsbereich haben attraktive<br>Rahmenverträge mit hohen Tarifleistungen und sehr guten Prämien schon jetzt für Sie ausgehandelt.</p>
  </div>
  <div class="btn" style="left:389px;top:1423px;width:199px;height:38px">PREISLISTE</div>

  <div class="proj" style="left:13px;top:1531px;width:298px;height:199px" role="img" aria-label="Zweigeschossiges weißes Stadthaus mit Walmdach und Vorgarten"></div>
  <div class="proj-head">UNSERE PROJEKTE</div>
  <div class="proj" style="left:326px;top:1584px;width:221px;height:146px" role="img" aria-label="Weißes Stadthaus in der Abenddämmerung mit beleuchteten Fenstern"></div>
  <div class="plan" role="img" aria-label="Grundriss eines Einfamilienhauses"></div>
  <div class="proj" style="left:724px;top:1531px;width:288px;height:199px" role="img" aria-label="Weißes Stadthaus mit Terrasse und Garten"></div>
  <svg class="plus" style="left:270px;top:1544px" viewBox="0 0 28 28" fill="none" stroke="#f9b91c" stroke-width="2"><circle cx="14" cy="14" r="12"/><path d="M14 8 V20 M8 14 H20"/></svg>
  <svg class="plus" style="left:505px;top:1593px" viewBox="0 0 28 28" fill="none" stroke="#f9b91c" stroke-width="2"><circle cx="14" cy="14" r="12"/><path d="M14 8 V20 M8 14 H20"/></svg>
  <svg class="plus" style="left:674px;top:1593px" viewBox="0 0 28 28" fill="none" stroke="#f9b91c" stroke-width="2"><circle cx="14" cy="14" r="12"/><path d="M14 8 V20 M8 14 H20"/></svg>
  <svg class="plus" style="left:973px;top:1544px" viewBox="0 0 28 28" fill="none" stroke="#f9b91c" stroke-width="2"><circle cx="14" cy="14" r="12"/><path d="M14 8 V20 M8 14 H20"/></svg>

  <div class="contact-card">
    <h4>KONTAKT</h4>
    <div class="info">
      <strong style="font-weight:500">KV Werkbau GmbH</strong><br>
      <strong style="font-weight:500">Lemar Bausatzhaus Partner</strong><br>
      <span style="display:block;height:21px"></span>
      Lindenallee 42<br>
      40210 Lindenfeld<br>
      Telefon: 01234-5678 900<br>
      E-mail: info@kvwerkbau.de<br>
      Geschäftsführer: Jonas Bergmann
    </div>
  </div>
  <div class="form">
    <div class="field" style="left:20px;top:20px;width:334px;height:38px">Name *</div>
    <div class="field" style="left:20px;top:78px;width:334px;height:38px">E-Mail *</div>
    <div class="field" style="left:20px;top:136px;width:334px;height:38px">Telefon</div>
    <div class="field" style="left:20px;top:194px;width:334px;height:38px">Postleitzahl / Ort *</div>
    <div class="field" style="left:374px;top:20px;width:343px;height:154px;padding-left:17px">Mitteilung</div>
    <div class="btn" style="left:454px;top:194px;width:200px;height:40px">SENDEN</div>
  </div>

  <footer class="footer">
    <div class="footer-logo"><span>LEMAR</span><span style="font-size:9px">Bausatzhaus</span></div>
    <h5 style="left:181px">INFORMATIONEN</h5>
    <div class="links" style="left:181px;top:51px">Datenschutz<br>Impressum</div>
    <h5 style="left:418px">MENU</h5>
    <div class="links" style="left:418px;top:51px">Über uns<br>Unsere Leistungen<br>Bauprojekte</div>
    <div class="links" style="left:552px;top:51px">Termine<br>Unsere Häuser<br>Kontakt</div>
    <h5 style="left:701px">SONSTIGE</h5>
    <div class="links" style="left:702px;top:45px">Downloads<br>Preiseliste<br>News</div>
    <div class="social" style="left:850px" role="img" aria-label="Soziales Netzwerk"></div>
    <div class="social" style="left:909px" role="img" aria-label="Soziales Netzwerk"></div>
  </footer>
</div>
</body>
</html>
```